Interior decorating services

I would like to have a business card created for my interior decorating business.

Target Market(s)

any one wishing to have their space decorated

Industry/Entity Type

Business

Contact Information for Business Card

Lorna J. Whitcombe ; 417-582-6094; quibfennet42@mailvoro.net

Font styles to use
Serif

Colors

Designer to choose colors to be used in the design.

Requirements
Must have
• nice colors that flow well, and the name of my business: NookWay Designs
Nice to have
• round logo looking design in the corner

```html
<!DOCTYPE html>
<html lang="en">
<head>
<meta charset="utf-8">
<title>NookWay Designs – Business Card</title>
<link rel="stylesheet" href="https://fonts.googleapis.com/css2?family=Libre+Baskerville:wght@400;700&display=swap">
<style>
  :root {
    --teal: #0e7670;
    --teal-dark: #0b635e;
    --grey: #a9a9a9;
    --grey-text: #9a9a9a;
    --paper: #ffffff;
    --backdrop: #e9ecec;
    --serif: "Libre Baskerville", Georgia, serif;
  }
  * { box-sizing: border-box; margin: 0; padding: 0; }
  html, body { width: 1200px; height: 880px; overflow: hidden; }
  body {
    background: var(--backdrop);
    font-family: var(--serif);
    position: relative;
  }
  .card {
    position: absolute;
    left: 285px;
    width: 630px;
    height: 360px;
    border-radius: 18px;
    overflow: hidden;
    box-shadow: 0 6px 18px rgba(0,0,0,.15);
  }
  /* Front */
  .card-front { top: 45px; background: var(--teal); }
  .front-brand {
    position: absolute;
    left: 0; right: 0; top: 0; bottom: 0;
    display: flex; align-items: center; justify-content: center; gap: 16px;
  }
  .brand-square {
    width: 34px; height: 34px;
    border: 6px solid var(--paper);
  }
  .front-brand .brand-name {
    color: var(--paper);
    font-size: 30px;
    font-weight: 700;
  }
  /* Back */
  .card-back { top: 475px; background: var(--paper); }
  .back-brand {
    position: absolute;
    left: 60px; top: 150px;
    display: flex; align-items: center; gap: 12px;
  }
  .back-brand .brand-square {
    width: 26px; height: 26px;
    border: 5px solid var(--teal);
  }
  .back-brand .brand-name {
    color: var(--teal);
    font-size: 23px;
    font-weight: 700;
  }
  .divider {
    position: absolute;
    left: 322px; top: 88px;
    width: 1px; height: 150px;
    background: var(--teal);
  }
  .contact-block {
    position: absolute;
    left: 352px; top: 95px;
  }
  .person-name {
    color: var(--teal);
    font-size: 22px;
    font-weight: 700;
  }
  .person-role {
    color: var(--grey-text);
    font-size: 13px;
    margin-top: 2px;
    margin-left: 12px;
  }
  .contact-list { list-style: none; margin-top: 42px; }
  .contact-item {
    display: flex; align-items: center; gap: 8px;
    color: var(--grey-text);
    font-size: 13px;
    line-height: 22px;
  }
  .contact-icon { width: 15px; height: 15px; flex: none; }
  .card-band {
    position: absolute; left: 0; bottom: 0;
    width: 630px; height: 90px;
  }
</style>
</head>
<body>

<section class="card card-front" aria-label="Card front">
  <div class="front-brand">
    <span class="brand-square"></span>
    <span class="brand-name">NookWay Designs</span>
  </div>
</section>

<section class="card card-back" aria-label="Card back">
  <div class="back-brand">
    <span class="brand-square"></span>
    <span class="brand-name">NookWay Designs</span>
  </div>

  <div class="divider"></div>

  <div class="contact-block">
    <p class="person-name">Lorna J. Whitcombe</p>
    <p class="person-role">Manager</p>
    <ul class="contact-list">
      <li class="contact-item">
        <svg class="contact-icon" viewBox="0 0 16 16" aria-hidden="true">
          <circle cx="8" cy="8" r="7" fill="none" stroke="#0e7670" stroke-width="1.3"/>
          <rect x="5.5" y="3.8" width="5" height="8.4" rx="1" fill="none" stroke="#0e7670" stroke-width="1.2"/>
        </svg>
        <span>417-582-6094</span>
      </li>
      <li class="contact-item">
        <svg class="contact-icon" viewBox="0 0 16 16" aria-hidden="true">
          <circle cx="8" cy="8" r="7.5" fill="#0e7670"/>
          <rect x="4" y="5.3" width="8" height="5.6" fill="#fff"/>
          <path d="M4 5.3 L8 8.6 L12 5.3" fill="none" stroke="#0e7670" stroke-width="1"/>
        </svg>
        <span>quibfennet42@mailvoro.net</span>
      </li>
    </ul>
  </div>

  <svg class="card-band" viewBox="0 0 630 90" aria-hidden="true">
    <path d="M0 72 L440 72 L452 58 L630 58 L630 64 L455 64 L443 78 L0 78 Z" fill="#a9a9a9"/>
    <path d="M0 80 L446 80 L458 66 L630 66 L630 90 L0 90 Z" fill="#0e7670"/>
    <path d="M455 52 L462 40 L630 40 L630 56 L452 56 Z" fill="#0e7670"/>
  </svg>
</section>

</body>
</html>
```